Taking a Paper and turning into a wonderful White Paper for Prospects and Clients

This is a white paper I need designed. I am including my company brochure so you can see the design/fonts being used and I'm including a white paper created - one that I like very much.

I am "NOT" looking for a cookie cutter white paper. I'm looking for a nice, clean design but with some creativity. Check out the white paper I included and you will get the idea.

Also included:
- the paper to be designed
- the paper to be designed "WITH" suggested design features such as carve outs, call outs and such

A few things I "DO NOT" like:
- images that are cheesy or corny
* people sitting at a table in a meeting
* Buildings

The white paper I included did not use pictures but had more design created by the firm. I like this approach and will probably give something like this more weight but is not required.
Updates

Reason: Realized time frame was too tight

Target Market(s)

Higher-End, wealthier clients

Industry/Entity Type

It Company

Requirements
Must have
• I DO NOT want the copy to be bunched together. The layout should flow where the copy is broken in the right spots to make reading easier. If you read a paper and it is just copy, interest is lost by everyone.
• COLORS: you can see from what I have included the colors I use
• My preference are very balanced colors using "clean spacing"

```html
<!DOCTYPE html>
<html lang="en">
<head>
<meta charset="utf-8">
<title>Ardenta White Paper – Fiduciary</title>
<link href="https://fonts.googleapis.com/css2?family=Josefin+Sans:wght@300;400;600;700&family=Raleway:wght@300;400&family=Source+Sans+3:wght@700&display=swap" rel="stylesheet">
<style>
  :root{
    --teal-deep:#1f4350;
    --teal-mid:#2b6670;
    --teal-ink:#234b56;
    --paper:#ffffff;
    --backdrop:#ffffff;
    --rule:#6d7c80;
    --body:#5b6669;
    --crowd:#c4c7c8;
    --cover-ink:#eef2f2;
  }
  *{margin:0;padding:0;box-sizing:border-box}
  html,body{width:1200px;height:521px;overflow:hidden;background:var(--backdrop)}
  .spread{position:relative;width:1200px;height:521px}
  .page{position:absolute;top:14px;width:368px;height:477px;background:var(--paper);box-shadow:2px 3px 6px rgba(0,0,0,.28);overflow:hidden}
  .page--cover{left:14px;background:radial-gradient(circle at 45% 50%,var(--teal-mid) 0%,var(--teal-deep) 70%)}
  .page--intro{left:406px}
  .page--body{left:804px}

  /* cover */
  .cover-title{position:absolute;left:50px;top:76px;font:300 25px/1.3 "Josefin Sans",sans-serif;color:var(--cover-ink)}
  .cover-title span{display:block}
  .cover-title .indent{padding-left:37px}
  .cover-sub{position:absolute;left:49px;top:163px;font:300 14px "Josefin Sans",sans-serif;color:var(--cover-ink)}
  .cover-brand{position:absolute;left:60px;top:250px;width:222px}
  .cover-brand .name{display:block;font:400 31px "Josefin Sans",sans-serif;letter-spacing:5px;color:var(--cover-ink)}
  .cover-brand .tagline{display:block;margin-top:2px;text-align:right;font:400 9.5px "Raleway",sans-serif;letter-spacing:1px;color:var(--cover-ink)}

  /* small header brand */
  .page-brand{position:absolute;left:25px;top:28px;font:600 7px "Josefin Sans",sans-serif;letter-spacing:1px;color:var(--teal-ink)}

  /* intro */
  .intro-mark{position:absolute;left:168px;top:86px}
  .intro-lead{position:absolute;left:50px;top:112px;font:300 13px/1.4 "Josefin Sans",sans-serif;color:var(--teal-ink)}
  .rule{position:absolute;left:48px;width:244px;height:1px;background:var(--rule)}
  .intro-question{position:absolute;left:49px;top:222px;font:300 18.5px/1.25 "Josefin Sans",sans-serif;color:var(--teal-ink)}
  .intro-question strong{font-weight:700}

  /* body page */
  .body-text{position:absolute;left:50px;width:274px;font:300 7.3px/1.35 "Raleway",sans-serif;color:var(--body)}
  .body-text p+p{margin-top:8px}
  .source-card{position:absolute;top:151px;width:128px;height:76px;border:1px solid #8a9497;padding:10px 8px 0 16px;font-family:"Raleway",sans-serif;color:#3e4649}
  .source-card .outlet{font-size:7.8px;font-weight:400}
  .source-card .author{font-size:5.6px;padding-left:6px}
  .source-card .headline{margin-top:9px;font-size:7px;line-height:1.35;font-weight:300;color:var(--body)}
  .remains{position:absolute;left:66px;top:276px;font:300 7.3px "Raleway",sans-serif;color:var(--body)}
  .big-question{position:absolute;left:172px;top:281px;font:700 14px/19px "Source Sans 3",sans-serif;color:var(--teal-ink)}
  .big-question span{display:block}
  .illustration{position:absolute;left:0;top:310px;width:176px;height:167px}
</style>
</head>
<body>
<main class="spread">

  <section class="page page--cover">
    <h1 class="cover-title"><span>Is your financial</span><span class="indent">advisor a fiduciary?</span></h1>
    <p class="cover-sub">It’s not that simple…</p>
    <div class="cover-brand"><span class="name">ARDENTA</span><span class="tagline">STEADY COUNSEL SINCE DAY ONE</span></div>
  </section>

  <section class="page page--intro">
    <div class="page-brand">ARDENTA</div>
    <svg class="intro-mark" width="8" height="4" viewBox="0 0 8 4"><path d="M1 1 Q4 4 7 1" fill="none" stroke="#234b56" stroke-width="1.4"/></svg>
    <p class="intro-lead">Well, we say, the question is not whether<br>your financial advisor is a fiduciary....</p>
    <div class="rule" style="top:206px"></div>
    <p class="intro-question">The question is whether your<br>financial advisor<br>is <strong>consistently acting</strong> in<br><strong>your best interest</strong>.</p>
    <div class="rule" style="top:335px"></div>
  </section>

  <section class="page page--body">
    <div class="page-brand">ARDENTA</div>
    <div class="body-text" style="top:68px">
      <p>As an investor, you’ve almost certainly heard talk about the differences between “the fiduciary standard” and “the suitability standard,” applied – varyingly – to advisers, brokers and other financial professionals.</p>
      <p>In fact, most likely you’ve heard it said – umpteen times – that unless your financial advisors are fiduciaries, required by law to adhere to the fiduciary standard, they won’t consistently act with your best interests in mind.</p>
    </div>
    <div class="source-card" style="left:49px">
      <div class="outlet">From FINANCE DAILY,</div>
      <div class="author">by Daniel Marsh:</div>
      <div class="headline">“Why Your Financial Advisor Should Be a Fiduciary”</div>
    </div>
    <div class="source-card" style="left:192px">
      <div class="outlet">From Evening Ledger,</div>
      <div class="author">by Peter Halvorsen:</div>
      <div class="headline">“Why you should make sure your financial advisor abides by the fiduciary standard”</div>
    </div>
    <p class="body-text" style="top:250px">Nonetheless, some investors may, for any number of reasons, still choose to hire professionals who work under the suitability standard.</p>
    <p class="remains">But, the question remains,</p>
    <h2 class="big-question">
      <span>should you only</span>
      <span style="padding-left:18px">hire an advisor</span>
      <span style="padding-left:31px">acting as a</span>
      <span style="padding-left:32px">fiduciary and avoid</span>
      <span style="padding-left:28px">those who are not?</span>
    </h2>
    <div class="illustration" role="img" aria-label="Illustration of a crowd of grey figures with a teal magnifying glass singling out one person" style="background:linear-gradient(100deg,var(--crowd) 0%,#b9c3c4 55%,var(--teal-mid) 100%)"></div>
  </section>

</main>
</body>
</html>
```